Landscaping Contract with customizable fillable form

Need a PDF Template with a format that can be filled in with info by us. Then sent to the customer for signature. form need to be able to be changed for each customer

Industry/Entity Type

Landscaping

Colors
00AB8E
00BBA5
67D7C9
C6EFE9
E9F9F6

```html
<!DOCTYPE html>
<html lang="en">
<head>
<meta charset="utf-8">
<title>Landscaping Contract Form</title>
<link href="https://fonts.googleapis.com/css2?family=Tinos:wght@400;700&display=swap" rel="stylesheet">
<style>
:root{
  --band-light:#c5e0b4;
  --band-dark:#548235;
  --header:#70ad47;
  --row-tint:#e2efd9;
  --rule:#c5e0b4;
  --green-text:#3f6b22;
  --body-text:#262626;
  --contract-text:#4f6b35;
  --page-edge:#d9d9d9;
}
*{box-sizing:border-box;margin:0;padding:0}
html,body{width:879px;height:1200px;overflow:hidden;background:#fff}
body{position:relative;font-family:"Tinos","Times New Roman",serif;color:var(--body-text)}
.sheet{position:absolute;width:386px;height:545px;background:#fff;border:1px solid var(--page-edge);overflow:hidden}
.sheet::before{content:"";position:absolute;left:0;right:0;top:0;height:9px;background:var(--band-light)}
.sheet::after{content:"";position:absolute;left:0;right:0;bottom:0;height:9px;background:var(--band-dark)}
.sheet--services{left:37px;top:39px}
.sheet--totals{left:446px;top:39px}
.sheet--turf{left:37px;top:601px}
.sheet--contract{left:446px;top:601px}

.brand{position:absolute;display:flex;align-items:center;gap:4px;color:var(--green-text);font-weight:700;font-size:8.5px;line-height:10px;width:72px}
.brand__dot{width:9px;height:9px;border-radius:50%;background:var(--band-dark);flex:none}
.divider{position:absolute;width:0;border-left:1px dotted #9bbb7f;height:40px}
.contact{position:absolute;color:var(--green-text);font-weight:700;font-size:6.4px;line-height:10.3px;white-space:nowrap}
.customer{position:absolute;left:220px;top:57px;color:var(--green-text);font-weight:700;font-size:6.4px;line-height:10.3px}
.customer span{display:flex;align-items:flex-end;gap:2px}
.customer i{display:block;border-bottom:1px dotted #9bbb7f;height:6px;font-style:normal}

table{position:absolute;border-collapse:collapse;table-layout:fixed;font-size:6.2px;line-height:7.4px}
td,th{border:0.6px solid var(--rule);padding:0 3px;vertical-align:middle;text-align:left;font-weight:400}
tr.tint td{background:var(--row-tint)}
thead th{background:var(--header);color:#fff;font-weight:700;text-align:center;height:8px;line-height:7px}
.section td{text-align:center;color:var(--green-text);font-weight:700}
.center{text-align:center}
.right{text-align:right}
ul{list-style:square;padding-left:7px}

.services{left:46px;top:116px;width:310px}
.totals{left:46px;top:46px;width:310px}
.totals .label{text-align:right;font-weight:700;background:var(--row-tint)}
.totals .label.plain{background:#fff}

.sign{position:absolute;top:291px;width:58px;border-top:0.8px solid var(--body-text)}
.sign span{position:absolute;top:7px;left:0;right:0;text-align:center;color:var(--green-text);font-weight:700;font-size:6.4px}

.turf{left:46px;top:115px;width:310px}
.turf .title th{background:var(--header);color:#fff;font-size:9.5px;height:11.5px;line-height:10px;text-align:center;border-color:var(--header)}
.turf .cols th{background:var(--row-tint);color:var(--green-text);font-weight:700;text-align:center;height:8.5px;line-height:7px}

.contract{position:absolute;left:47px;width:292px;color:var(--contract-text);font-size:6.3px;line-height:8.1px;text-align:justify}
.contract-title{position:absolute;left:47px;top:46px;color:var(--green-text);font-weight:700;font-size:8px}
.blank{display:inline-block;border-bottom:0.6px solid var(--contract-text);height:6px}
.sigline{position:absolute;border-top:0.6px solid var(--contract-text)}
.siglabel{position:absolute;color:var(--contract-text);font-size:6.3px}
</style>
</head>
<body>

<section class="sheet sheet--services">
  <div class="brand" style="left:46px;top:63px"><span class="brand__dot"></span><span>Greenmeadow Estates</span></div>
  <div class="divider" style="left:120px;top:52px"></div>
  <div class="contact" style="left:132px;top:56px">Daniel Marsh<br>555-014-2276<br>info@greenmeadow.co</div>
  <div class="divider" style="left:206px;top:52px"></div>
  <div class="customer">
    <span>Customer <i style="width:93px"></i></span>
    <span>Address <i style="width:100px"></i></span>
    <span style="padding-left:25px"><i style="width:100px"></i></span>
  </div>

  <table class="services">
    <colgroup><col style="width:53px"><col style="width:146px"><col style="width:64px"><col style="width:47px"></colgroup>
    <thead><tr><th>Service</th><th>Description</th><th>Dates</th><th>Price</th></tr></thead>
    <tbody>
      <tr class="section" style="height:13.8px"><td colspan="4">Landscape Services</td></tr>
      <tr style="height:22.9px"><td>Lawn Cuts</td><td>30 Cuts- Includes mowing, line trimming, and blowing of decks and walkways. We adjust mowing height based on your grass variety and time of year.</td><td></td><td></td></tr>
      <tr class="tint" style="height:16.5px"><td>Spring Clean-up</td><td>Overall Clean-up of property. Removal of all leftover debris from winter</td><td></td><td></td></tr>
      <tr style="height:16.5px"><td>Mulch Labour</td><td>Labour for edging, prepping, and applying mulch.</td><td></td><td></td></tr>
      <tr class="tint" style="height:16.5px"><td>Mulch Materials</td><td>Mulch @ $44 per yard delivered.</td><td></td><td></td></tr>
      <tr style="height:16.5px"><td>Weed Control Spray</td><td>5 Applications throughout the season to control weeds in : Beds, Driveways, Walkways and Patios</td><td></td><td></td></tr>
      <tr class="tint" style="height:38.3px"><td>Trimming</td><td>Trim and shape of all necessary plantings. Clean-up and removal of all debris. Clean-up and removal of all debris. Done x2 per year. June/July after strong new growth is complete and September/October after seasonal growth is complete</td><td></td><td></td></tr>
      <tr style="height:19.2px"><td>Early Fall Clean-up</td><td>Light clean-up in early/mid November to help mitigate excess leaf build up throughout property.</td><td></td><td></td></tr>
      <tr class="tint" style="height:16px"><td>Fall Clean-up</td><td>Removal of leaves and debris, cutting back of all necessary plantings</td><td></td><td></td></tr>
      <tr style="height:59.6px"><td>Estate Hours</td><td>Estimated labour hours to be used throughout the season for:<ul><li>Hand weeding sensitive areas that cannot be managed by weed control spray</li><li>Fertilizing necessary annuals and perennials</li><li>Light Trimming, Dead Heading annuals and perennials</li><li>Raking stone driveway (Where applicable)</li></ul></td><td class="center">$60/hour</td><td class="center">Billed additionally each month</td></tr>
      <tr class="tint" style="height:17px"><td>Annuals</td><td>A great way to add seasonal color throughout property</td><td class="center">Contact for pricing</td><td></td></tr>
      <tr style="height:17px"><td>Flower Pots</td><td>A great way to add seasonal color around pools, patios and entrances</td><td class="center">Contact for pricing</td><td></td></tr>
      <tr class="tint" style="height:17px"><td>Gutter Cleaning</td><td>Removal of debris from gutters during fall cleanup.</td><td></td><td></td></tr>
      <tr style="height:18.6px"><td>Miscellaneous Work</td><td></td><td></td><td></td></tr>
      <tr class="section" style="height:17px"><td colspan="4">Plant Health</td></tr>
      <tr style="height:25px"><td>Tree and shrub Fertilization</td><td>Essential feeding for all necessary trees and shrubs.</td><td></td><td></td></tr>
      <tr class="tint" style="height:17px"><td>Doormant Oil</td><td>A widely effective insect control. Elimates insects at the egg stage. Applied once during March/April</td><td></td><td></td></tr>
      <tr style="height:11.7px"><td>Summer Deer</td><td>Summer Deer spray done monthly for control. For all</td><td></td><td></td></tr>
    </tbody>
  </table>
</section>

<section class="sheet sheet--totals">
  <table class="totals">
    <colgroup><col style="width:52px"><col style="width:146px"><col style="width:64px"><col style="width:48px"></colgroup>
    <tbody>
      <tr style="height:15.4px"><td>Spray</td><td>necessary plantings April-October 7x</td><td></td><td></td></tr>
      <tr class="tint" style="height:15.4px"><td>Winter Deer Spray</td><td>A highly effective long lasting deer spray used for control in winter months. Done 1x in November</td><td></td><td></td></tr>
      <tr class="section" style="height:20.2px"><td colspan="4">Irrigation</td></tr>
      <tr class="tint" style="height:15.4px"><td>Open Irrigation System Type</td><td>Turning on water, setting clock, checking all zones.</td><td></td><td></td></tr>
      <tr style="height:15.4px"><td>Winterization of Irrigation</td><td>Clearing irrigation system of water and shutting off main valve.</td><td></td><td></td></tr>
      <tr class="tint" style="height:22.9px"><td>Yearly Maintanance of Irrigation</td><td>Includes seasonal adjustments and monitoring of clock.</td><td></td><td></td></tr>
      <tr style="height:22.9px"><td>Turf Management Program</td><td>See page 2 for complete breakdown.</td><td></td><td></td></tr>
      <tr class="tint" style="height:30.3px"><td>Tick &amp; Mosquito Spray</td><td>Pricing reflects traditional applications done monthly April-September. Organic options offered. Please contact us and we'd be happy to discuss options that fit your needs best.</td><td></td><td></td></tr>
      <tr style="height:12.8px"><td colspan="2" rowspan="4" style="vertical-align:top;padding-top:1px">Pay in full by March 15<sup style="font-size:4px">th</sup></td><td class="label plain">Subtotal</td><td></td></tr>
      <tr style="height:13.3px"><td class="label">Tax</td><td style="background:var(--row-tint)"></td></tr>
      <tr style="height:12.8px"><td class="label plain">Total</td><td></td></tr>
      <tr style="height:13.3px"><td class="label">1 Payment</td><td style="background:var(--row-tint)"></td></tr>
    </tbody>
  </table>
  <div class="sign" style="left:46px"><span>Signature</span></div>
  <div class="sign" style="left:280px"><span>Date</span></div>
</section>

<section class="sheet sheet--turf">
  <div class="brand" style="left:46px;top:62px"><span class="brand__dot"></span><span>Greenmeadow Estates</span></div>
  <div class="divider" style="left:118px;top:52px"></div>
  <div class="contact" style="left:129px;top:56px">Daniel Marsh<br>555-014-2276<br>info@greenmeadow.co</div>

  <table class="turf">
    <colgroup><col style="width:47px"><col style="width:152px"><col style="width:64px"><col style="width:47px"></colgroup>
    <thead>
      <tr class="title"><th colspan="4">ESTATE TURF PROGRAM</th></tr>
      <tr class="cols"><th>Service</th><th>Description</th><th>Dates</th><th>Price</th></tr>
    </thead>
    <tbody>
      <tr style="height:16.5px"><td>Early Spring</td><td>Complete, granular fertilizer and pre-emergent crabgrass control</td><td class="center">April 1 - April 22</td><td></td></tr>
      <tr class="tint" style="height:17px"><td>Spring</td><td>Complete, granular fertilizer with iron and broadleaf control</td><td class="center">April 23 - May 13</td><td></td></tr>
      <tr style="height:17px"><td>Early Summer</td><td>Complete, granular fertilizer with iron and broadleaf control</td><td class="center">June 4 - June 24</td><td></td></tr>
      <tr class="tint" style="height:16px"><td>Late Summer</td><td>Post-emergent crabgrass and late summer weed control</td><td class="center">June 16 - Aug 5</td><td></td></tr>
      <tr style="height:16.5px"><td>Early Fall</td><td>Complete balanced fertilizer with iron and weed control</td><td class="center">Aug 20 - Sept 9</td><td></td></tr>
      <tr class="tint" style="height:12.2px"><td>Late Fall</td><td>Granular Fertilizer w/ high potassium to winterize lawn</td><td class="center">Oct 1 - Oct 31</td><td></td></tr>
      <tr style="height:42px"><td>Aeration</td><td>Due to the constant compaction of soil from mowing and foot traffic, we recommend a yearly aeration of the lawn. It helps get nutrients, water and air down to the roots of the soil. Creates strong root growth. Vital Service for a superior lawn.</td><td class="center">Aug 20 - Oct 15</td><td></td></tr>
      <tr class="tint" style="height:14.4px"><td>Grub Control</td><td>Highly effective, preventive treatment for grub control.</td><td class="center">Mid Summer</td><td></td></tr>
      <tr style="height:15.4px"><td>Lime</td><td>Essential application to maintain proper PH of soil.</td><td class="center">Early Spring or Late fall</td><td></td></tr>
      <tr class="tint" style="height:17px"><td>Fungicide</td><td>Preventive and curative treatment for various turf diseases.</td><td class="center">Throughout season</td><td></td></tr>
      <tr style="height:16.5px"><td>Nutledge</td><td>Highly effective treatment for nutsedge (Fast growing, unsightly yellow weed)</td><td class="center">Mid Summer</td><td></td></tr>
      <tr class="tint" style="height:17px"><td>Bent grass</td><td>Specialty Application for treatment of unsightly spreading creeping bent grass.</td><td></td><td></td></tr>
      <tr style="height:34px"><td>Slit-Seeding</td><td>Guaranteed method of slicing the soil to sew new seed directly into soil. Custom seed blend specific to your property. Done in a crisscross pattern for complete coverage.</td><td></td><td></td></tr>
      <tr class="tint" style="height:25px"><td>Over seeding</td><td>Broadcast method of incorporating seed immediately after core aeration to replenish old lawn with new seedlings. Recommended yearly.</td><td></td><td></td></tr>
      <tr style="height:17px"><td>Soil Samples</td><td>Essential service, provides us with lab results of soil structure to effectively bring soil to proper alignment.</td><td></td><td></td></tr>
      <tr class="tint" style="height:13.3px"><td></td><td class="right">TOTAL</td><td></td><td></td></tr>
    </tbody>
  </table>
</section>

<section class="sheet sheet--contract">
  <h1 class="contract-title">Yard Work Contract</h1>
  <p class="contract" style="top:61px">This contract is made between <span class="blank" style="width:85px"></span>. (hereafter known as the Client) and <span class="blank" style="width:94px"></span>(hereafter known as the Contractor). The Client desires to have certain maintenance services, described below, performed upon a yard located at <span class="blank" style="width:75px"></span>. Therefore, the parties hereby agree as follows:</p>
  <p class="contract" style="top:99px">1. Client shall grant Contractor access to the yard and its surroundings during regular business hours and other mutually agreeable times.</p>
  <p class="contract" style="top:120px">2. (Client or Contractor) shall provide all equipment and consumable supplies necessary to perform maintenance services on the yard.</p>
  <p class="contract" style="top:141px">3. Client shall pay Contractor $X on the first day of each (week or month) for regular maintenance services to be performed during the rest of that (week or month). See "Regular Maintenance" description below.</p>
  <p class="contract" style="top:163px">4. Client shall pay Contractor for any additional maintenance or repair work that may become necessary to maintain a pleasing, safe, and horticulturally healthy yard (hereafter known as "ad hoc work"). Contractor shall bill Client for the cost of ad hoc work and Client shall include payment with Client's next payment for regular maintenance.</p>
  <p class="contract" style="top:200px">5. Ad hoc work whose cost is less than $50 may be performed by Contractor without Clients explicit authorization. Work which Contractor estimates will cost $50 or more shall be authorized by Client before it is performed.</p>
  <p class="contract" style="top:230px">6. "Regular Maintenance" shall include removal of debris from the yard; mowing of lawn and trimming of shrubs, trees, and other plants; fertilization and other conditioning of the yard's soil; inspection of plants and soil for pests, and extermination of any pests discovered.</p>
  <p class="contract" style="top:259px">7. Contractor shall begin performing regular maintenance on MM/DD/YYYY. Thereafter, regular maintenance shall be performed on a schedule to which the parties agree.</p>
  <p class="contract" style="top:280px">8. Either party may terminate this agreement with written notice to the other party. Any payment for services rendered owed by Client shall be due and payable at the time this agreement is terminated.</p>
  <p class="contract" style="top:302px">In witness to their agreement to these terms, the Client and Contractor affix their signatures below.</p>

  <div class="sigline" style="left:47px;top:334px;width:64px"></div>
  <div class="sigline" style="left:140px;top:334px;width:78px"></div>
  <div class="siglabel" style="left:47px;top:337px">Client's signature,</div>
  <div class="siglabel" style="left:140px;top:337px">date</div>
  <div class="sigline" style="left:47px;top:368px;width:64px"></div>
  <div class="sigline" style="left:140px;top:368px;width:78px"></div>
  <div class="siglabel" style="left:47px;top:371px">Contractor's Signature,</div>
  <div class="siglabel" style="left:140px;top:371px">date</div>
  <div class="sigline" style="left:47px;top:403px;width:139px"></div>
  <div class="siglabel" style="left:47px;top:406px">Client's printed name</div>
</section>

</body>
</html>
```